Enrollment openings for summer

I need a postcard design to promote openings at my school. I currently have Crestline Press print all of my business cards and have my website with Crestline Press, I would like to stick with the design I have. Brightfield School is a therapeutic day school servicing 6-12th grade for bright students with emotional disabilities, autism, learning disabilities and OHI. Although I am trying to promote openings it is not necessarily appropriate for this to be an "upbeat" promotion, more of a softer feel as students come to me when they are struggling significantly and need a safe place to receive an education and support for emotional stability. I will have openings to serve all grades beginning June 3rd (ESY) and for the 15-16 school year. I would also like to communicate that districts can schedule a tour or call for more information. I am looking to market in a 30 miles radius to schools, psychologists, social workers, etc...PLEASE use the look and feel of my current website www.bfsweb.example

Target Market(s)

schools, psychologists, hospital programs, social workers

Industry/Entity Type

Business

Font styles to use
Serif
Decorative

Requirements
Must have
• must match our current design with color and logo, easy to read font
Should not have
• slang, be too bold, softer comfortable feel

```html
<!DOCTYPE html>
<html lang="en">
<head>
<meta charset="utf-8">
<title>Brightfield School – Enrollment Postcard</title>
<link href="https://fonts.googleapis.com/css2?family=Tinos:ital,wght@0,400;0,700;1,400;1,700&display=swap" rel="stylesheet">
<style>
  :root {
    --maroon: #8a1c3c;
    --maroon-deep: #6e1530;
    --brown: #4a2619;
    --parchment: #d8c39e;
    --parchment-light: #e6d6b8;
    --parchment-dark: #b89c72;
    --flourish: rgba(120, 88, 52, .42);
    --ink: #3a271c;
    --paper: #ffffff;
    --rule: #b9b1aa;
    --stage: #ece8e2;
  }
  * { box-sizing: border-box; margin: 0; padding: 0; }
  html, body { width: 1200px; height: 625px; overflow: hidden; }
  body {
    background: var(--stage);
    font-family: "Tinos", "Times New Roman", serif;
    position: relative;
  }
  .postcard {
    position: absolute;
    top: 105px;
    width: 560px;
    height: 415px;
    overflow: hidden;
    box-shadow: 0 4px 14px rgba(0,0,0,.18);
  }

  /* ---------- Front ---------- */
  .postcard--front {
    left: 30px;
    background: radial-gradient(ellipse at 45% 45%, var(--parchment-light) 0%, var(--parchment) 60%, var(--parchment-dark) 100%);
  }
  .flourish {
    position: absolute;
    border-radius: 50%;
    background: radial-gradient(ellipse, var(--flourish) 0%, rgba(120,88,52,.18) 45%, rgba(120,88,52,0) 72%);
  }
  .flourish--top { top: -20px; left: 170px; width: 230px; height: 100px; }
  .flourish--right { top: 70px; right: -30px; width: 190px; height: 90px; }
  .flourish--bottom { bottom: -25px; left: -20px; width: 260px; height: 130px; }
  .brand {
    position: absolute;
    top: 24px;
    left: 24px;
    color: var(--maroon);
    font-size: 32px;
    font-weight: 400;
    letter-spacing: .5px;
  }
  .tagline-tab {
    position: absolute;
    top: 20px;
    right: 0;
    background: var(--brown);
    color: var(--paper);
    font-weight: 700;
    font-size: 17px;
    padding: 7px 16px 7px 18px;
    outline: 1px solid rgba(255,255,255,.55);
    outline-offset: -4px;
  }
  .headline {
    position: absolute;
    top: 90px;
    left: 24px;
    width: 380px;
    color: var(--maroon);
    font-size: 34px;
    font-weight: 700;
    line-height: 1.08;
  }
  .subhead {
    position: absolute;
    top: 172px;
    left: 24px;
    width: 330px;
    color: var(--ink);
    font-size: 13.5px;
    font-weight: 700;
    line-height: 1.2;
  }
  .intro {
    position: absolute;
    top: 208px;
    left: 24px;
    width: 340px;
    color: var(--maroon);
    font-size: 12.5px;
    font-style: italic;
    line-height: 1.18;
  }
  .season-note {
    position: absolute;
    top: 306px;
    left: 24px;
    width: 360px;
    color: var(--ink);
    font-size: 12px;
    font-weight: 700;
  }
  .seal {
    position: absolute;
    top: 148px;
    right: 36px;
    width: 128px;
    height: 128px;
    border-radius: 50%;
    background: var(--maroon);
    border: 3px dotted var(--parchment-light);
    display: flex;
    align-items: center;
    justify-content: center;
  }
  .seal__inner {
    width: 100px;
    height: 100px;
    border-radius: 50%;
    background: var(--parchment-light);
    border: 2px solid var(--parchment-dark);
    display: flex;
    align-items: center;
    justify-content: center;
    text-align: center;
    color: var(--maroon);
    font-size: 13px;
    font-weight: 700;
    line-height: 1.15;
    padding: 6px;
  }
  .seal__inner em { display: block; font-style: italic; }
  .address-line {
    position: absolute;
    bottom: 64px;
    right: 22px;
    color: var(--ink);
    font-size: 11px;
  }
  .phone-band {
    position: absolute;
    right: 0;
    bottom: 0;
    width: 330px;
    height: 58px;
  }
  .phone-band svg { position: absolute; inset: 0; }
  .phone-band__number {
    position: absolute;
    right: 22px;
    bottom: 6px;
    color: var(--paper);
    font-size: 40px;
    font-weight: 700;
    letter-spacing: .5px;
  }

  /* ---------- Back ---------- */
  .postcard--back {
    left: 610px;
    background: var(--paper);
    border: 1px solid #ddd;
  }
  .postcard--back .brand { top: 30px; }
  .back-tagline {
    position: absolute;
    top: 92px;
    left: 24px;
    color: var(--maroon);
    font-size: 15px;
    font-weight: 700;
  }
  .contact-band {
    position: absolute;
    top: 132px;
    left: 0;
    width: 320px;
    height: 122px;
    background: var(--maroon-deep);
    color: var(--paper);
    padding: 10px 0 0 22px;
  }
  .contact-band__title { font-size: 14px; font-weight: 700; }
  .contact-band__address { font-size: 11.5px; margin-top: 2px; }
  .contact-band__phone { font-size: 30px; font-weight: 700; line-height: 1.1; margin-top: 4px; }
  .contact-band__web { font-size: 14px; font-weight: 700; }
  .map {
    position: absolute;
    top: 262px;
    left: 10px;
    width: 300px;
    height: 86px;
    background: linear-gradient(135deg, #eef0ec 0%, #dfe3e0 100%);
    border: 1px solid #d0d0d0;
  }
  .tour-note {
    position: absolute;
    top: 356px;
    left: 22px;
    width: 290px;
    color: var(--maroon);
    font-size: 12px;
    font-weight: 700;
    line-height: 1.25;
  }
  .stamp-box {
    position: absolute;
    top: 22px;
    right: 28px;
    width: 70px;
    height: 82px;
    border: 1.5px solid var(--rule);
  }
  .address-rules {
    position: absolute;
    top: 150px;
    left: 345px;
    width: 190px;
    list-style: none;
  }
  .address-rules li {
    height: 28px;
    border-bottom: 1.5px solid var(--rule);
  }
  .swoosh {
    position: absolute;
    inset: 0;
    pointer-events: none;
  }
</style>
</head>
<body>

  <section class="postcard postcard--front" aria-label="Postcard front">
    <div class="flourish flourish--top" role="img" aria-label="Soft floral scroll ornament"></div>
    <div class="flourish flourish--right" role="img" aria-label="Soft floral scroll ornament"></div>
    <div class="flourish flourish--bottom" role="img" aria-label="Soft floral scroll ornament"></div>

    <div class="brand">Brightfield School</div>
    <div class="tagline-tab">Where Bright Students Shine!</div>

    <h1 class="headline">Openings in Junior High and High School</h1>
    <p class="subhead">A Therapeutic Day School for Students with Social and Emotional Challenges</p>
    <p class="intro">Serving the needs of students with Emotional Disabilities, Learning Disabilities, Autism and Other Health Impairments since September, 2000. We provide a safe, therapeutic, and educational environment for students whose disabilities impair their academic ability despite average to above average academic potential.</p>
    <p class="season-note">Openings begin June 3rd (ESY) and for the 15-16 school year.</p>

    <div class="seal">
      <div class="seal__inner"><span><em>Scheduling</em>intake now! Call for more information.</span></div>
    </div>

    <p class="address-line">1420 W. Linden Street • Maple Grove, IL • <strong>www.bfsweb.example</strong></p>

    <div class="phone-band">
      <svg width="330" height="58" viewBox="0 0 330 58" aria-hidden="true">
        <path d="M0 58 C30 58 20 0 60 0 L330 0 L330 58 Z" fill="var(--brown)"/>
      </svg>
      <div class="phone-band__number">555.014.0463</div>
    </div>
  </section>

  <section class="postcard postcard--back" aria-label="Postcard back">
    <svg class="swoosh" width="560" height="415" viewBox="0 0 560 415" aria-hidden="true">
      <path d="M560 150 C470 210 360 250 330 415 L350 415 C385 270 480 225 560 180 Z" fill="var(--parchment)"/>
      <path d="M560 185 C480 235 400 280 375 415 L410 415 C430 300 500 255 560 225 Z" fill="var(--brown)"/>
    </svg>

    <div class="brand">Brightfield School</div>
    <p class="back-tagline">Where Bright Students Shine!</p>

    <div class="contact-band">
      <p class="contact-band__title">Contact us today!</p>
      <p class="contact-band__address">1420 W. Linden Street • Maple Grove, IL</p>
      <p class="contact-band__phone">555.014.0463</p>
      <p class="contact-band__web">www.bfsweb.example</p>
    </div>

    <div class="map" role="img" aria-label="Street map showing the school location"></div>
    <p class="tour-note">Districts are welcome to schedule a tour or call for more information.</p>

    <div class="stamp-box" aria-label="Stamp area"></div>
    <ul class="address-rules" aria-label="Mailing address lines">
      <li></li><li></li><li></li><li></li><li></li><li></li>
    </ul>
  </section>

</body>
</html>
```